CraftNest needs a full wrap product packaging design. Outer and inner + inner product nesting/inserts

We need a complete product packaging design with outer and inner packaging with inner product nesting/inserts ready to print and fabricate. The package to use paperboard, cardboard.

We pretty much know what we need for the outer box, the banner horizontal (.psd) on top , craftnest logo on one side, and the rest plain black or white! All the illustrator and photoshop files are provided.
What we don't have is the inner design and nesting of the 3 items and all the files to print and fabricate.

The product is an Artwork canvas size 40x50x2cm that comes with a certificate of authenticity ( a card 10x12cm) and a little container containing a figurine (the one from the artwork, a tiny astronaut!) size of the container 7x5x2.26cm
The experience and feel should be playful / premium
We provide the top box logo in .psd and all the logo and text necessary. Including as well a SketchUp file of the 3 items (canvas, card, container+figurine inside) to give you an idea of what the box contains.

I did order the same on Taskoro but the designer only could deliver the outer design and not the inner + product inserts/nesting so he had to cancel it. i'll attach his design for reference we liked but it wasn't at scale, feel free to create something different. As long as the banner is on the top side and the logo on one side
Have a look at this video which should give you a good idea of what we are looking for https://www.vidstreamo.example/watch?v=QxT4kk8zLwa

it is important to present the 3 items inside, well nested within custom-fit compartments/inserts/nest, and keep the box to its minimum size while keeping enough space to have the item space to breathe and perhaps some cool text or design in the inner packaging design.

Design requirements:
Stonemillicent logo + artworks patchwork on the top of the box (craftnest banner .psd chose one of 2 with a preference for the horizontal)
Craftnest logo on one side only. Possible to change the LAB color white or black
contains all 3 items ( canvas + certificate card + container )
To be added on the box top the wording "Collection 2021" in Gotham Font (same as Stone Millicent) This would be smaller than Stone Millicent wording.

Feel free to check the artist page on our website for additional inspiration
https://craftnest.example/stonemillicent
password: stone

Target Market(s)

Art collector, art lovers

Industry/Entity Type

Art

Font styles to use
Other font styles liked:
• Gotham (same as stone millicent on the .psd)

Requirements
Must have
• Mockup, inner and outer design + inner product inserts/nesting, files necessary for print + fabrication
Nice to have
• Originality simplicity

```html
<!DOCTYPE html>
<html lang="en">
<head>
<meta charset="utf-8">
<title>Stone Millicent – Inner Tray Dieline</title>
<link rel="stylesheet" href="https://fonts.googleapis.com/css2?family=Montserrat:wght@300;400&family=Roboto+Condensed:wght@300&display=swap">
<style>
  :root {
    --canvas: #ffffff;
    --board: #282a29;
    --window: #fdfdfd;
    --cut: #e0262b;
    --fold: #1ea0dc;
    --mark: #1d6a80;
    --ink-light: #ffffff;
    --ink-soft: #c9cbcb;
  }
  html, body {
    margin: 0;
    padding: 0;
    width: 1200px;
    height: 1200px;
    overflow: hidden;
    background: var(--canvas);
  }
  .dieline {
    display: block;
    width: 1200px;
    height: 1200px;
  }
  .board { fill: var(--board); }
  .fold-line {
    fill: none;
    stroke: var(--fold);
    stroke-width: 1;
    stroke-dasharray: 9 7;
  }
  .cut-window {
    fill: var(--window);
    stroke: var(--cut);
    stroke-width: 2;
  }
  .cut-notch {
    fill: none;
    stroke: var(--cut);
    stroke-width: 1.6;
  }
  .brand-disc { fill: var(--ink-light); }
  .brand-name {
    font-family: "Montserrat", sans-serif;
    font-weight: 400;
    font-size: 14px;
    fill: var(--ink-light);
    text-anchor: middle;
  }
  .caption {
    font-family: "Montserrat", sans-serif;
    font-weight: 300;
    font-size: 8px;
    letter-spacing: 0.3px;
    fill: var(--ink-soft);
    text-anchor: middle;
  }
  .measure-line {
    stroke: var(--mark);
    stroke-width: 1.6;
  }
  .measure-label {
    font-family: "Roboto Condensed", sans-serif;
    font-weight: 300;
    font-size: 30px;
    fill: var(--mark);
  }
</style>
</head>
<body>
<svg class="dieline" viewBox="0 0 1200 1200" xmlns="http://www.w3.org/2000/svg" aria-label="Inner tray dieline for the Stone Millicent collection box">
  <!-- board net -->
  <g class="tray-net">
    <rect class="board" x="150" y="114" width="907.5" height="979"/>
    <rect class="board" x="95" y="170" width="1017.5" height="868"/>
    <rect class="fold-line" x="150.5" y="170" width="907" height="868"/>
  </g>

  <!-- canvas compartment -->
  <rect class="cut-window canvas-nest" x="192" y="209.5" width="631" height="788.5"/>

  <!-- brand mark -->
  <g class="brand">
    <circle class="brand-disc" cx="939" cy="336" r="47"/>
    <text class="brand-name" x="939" y="402" letter-spacing="4">STONE</text>
    <text class="brand-name" x="939" y="418" letter-spacing="1.5">MILLICENT</text>
  </g>

  <!-- finger notches for certificate card -->
  <path class="cut-notch" d="M857 580.5 H860 A23.5 23.5 0 0 1 860 627.5 H857"/>
  <path class="cut-notch" d="M1021 580.5 H1018 A23.5 23.5 0 0 0 1018 627.5 H1021"/>
  <text class="caption" x="939" y="720">certificate of authenticity</text>

  <!-- figurine container compartment -->
  <rect class="cut-window container-nest" x="899.5" y="812.5" width="78.5" height="110"/>
  <text class="caption" x="939" y="946">tiny little things</text>

  <!-- spacing notes -->
  <g class="measure">
    <text class="measure-label" x="1121" y="739">14px</text>
    <line class="measure-line" x1="1047.5" y1="751" x2="1177.5" y2="751"/>
    <text class="measure-label" x="1117" y="954">14px</text>
    <line class="measure-line" x1="1043" y1="965" x2="1173" y2="965"/>
  </g>
</svg>
</body>
</html>
```